Dorvelan Swimming & Athletics Center

We need Business Card for a Athletics center
The logo frome the Uploaded Files ( b card fimal)
Οn one side of card we need the logo of company the Contact and the website:
1. Address:(Limassol, Cyprus 12-14 Stavrinelou str,Ano Trimeni,P.C. 4832)

2.Phone number: (+357) 25-704263

3. Mail: info@dorvelanfit.example

3. Website: www.dorvelanfit.example

Οn the other side of the card we need to write the sport of the company:

1. Artistic Gymnastics
2. Swimming
3. Gym - Fitness
4. Programs
5. Dancing
5.Tennis

From the Uploaded Files you can get the logo.In a logo is behind the black color which can be removed from logo.

Υou can use that color you want.
.
Updates

Industry/Entity Type

Business

Font styles to use
Decorative

Colors
0555a3
ffcf3e
3176b5
0692cd
add136
f04a50
000000
cfcfcf
9d9d9d

Requirements
Should not have
• photos with faces
• photo fro the Website:www.dorvelanfit.example

```html
<!DOCTYPE html>
<html lang="en">
<head>
<meta charset="utf-8">
<title>Dorvelan Swimming &amp; Athletics Center – Business Card</title>
<link rel="stylesheet" href="https://fonts.googleapis.com/css2?family=EB+Garamond:wght@400;600;700&display=swap">
<style>
  :root {
    --backdrop: #2b2b2b;
    --card: #f7f7f7;
    --card-edge: #e4e4e4;
    --accent: #f0a21a;
    --accent-light: #ffcf3e;
    --ink: #2a2a2a;
    --ink-soft: #444444;
    --badge: #1c1c1c;
  }
  * { box-sizing: border-box; margin: 0; padding: 0; }
  html, body { width: 1200px; height: 873px; overflow: hidden; }
  body {
    background: var(--backdrop);
    font-family: "EB Garamond", Georgia, serif;
    color: var(--ink);
    position: relative;
  }
  .card {
    position: absolute;
    width: 540px;
    height: 318px;
    background: var(--card);
    border: 1px solid var(--card-edge);
    border-radius: 18px;
    overflow: hidden;
  }
  .card--front { left: 40px; top: 278px; }
  .card--back  { left: 620px; top: 278px; }

  .brand {
    position: absolute;
    display: flex;
    align-items: center;
    gap: 14px;
  }
  .brand__name {
    font-weight: 700;
    font-size: 58px;
    letter-spacing: 3px;
    color: var(--accent);
    line-height: 1;
  }
  .brand__badge {
    width: 58px; height: 58px;
    border-radius: 50%;
    background: var(--badge);
  }
  .card--front .brand { right: 34px; top: 112px; }
  .card--back .brand { right: 34px; top: 40px; }
  .card--back .brand__name { font-size: 50px; }
  .card--back .brand__badge { width: 52px; height: 52px; }

  .sports {
    position: absolute;
    left: 0; right: 0; bottom: 30px;
    display: flex;
    justify-content: center;
    gap: 16px;
    font-size: 17px;
    color: var(--ink);
  }

  .holder {
    position: absolute;
    left: 40px; top: 186px;
    width: 200px;
    text-align: center;
  }
  .holder__name { font-weight: 600; font-size: 22px; color: var(--accent); }
  .holder__role { font-size: 16px; color: var(--ink-soft); margin-top: 2px; }
  .holder__web { font-weight: 700; font-size: 16px; margin-top: 18px; }

  .divider {
    position: absolute;
    left: 262px; top: 150px;
    width: 3px; height: 130px;
    background: linear-gradient(to bottom, rgba(240,162,26,0), var(--accent) 40%, rgba(240,162,26,0));
  }

  .contact {
    position: absolute;
    left: 286px; top: 150px;
    list-style: none;
    font-size: 16px;
    color: var(--ink);
  }
  .contact__item {
    display: flex;
    align-items: flex-start;
    gap: 12px;
    margin-bottom: 12px;
    line-height: 1.2;
  }
  .contact__icon { width: 18px; height: 18px; flex: none; fill: var(--accent); margin-top: 1px; }
</style>
</head>
<body>

  <section class="card card--front" aria-label="Card front">
    <div class="brand">
      <span class="brand__name">DORVELAN</span>
      <span class="brand__badge"></span>
    </div>
    <p class="sports">
      <span>Artistic Gymnastics</span>
      <span>Swimming</span>
      <span>Gym</span>
      <span>Fitness Programs</span>
      <span>Dancing</span>
      <span>Tennis</span>
    </p>
  </section>

  <section class="card card--back" aria-label="Card back">
    <div class="brand">
      <span class="brand__name">DORVELAN</span>
      <span class="brand__badge"></span>
    </div>

    <div class="holder">
      <p class="holder__name">Andreas Kyrou</p>
      <p class="holder__role">Owner / Founder</p>
      <p class="holder__web">www.dorvelanfit.example</p>
    </div>

    <div class="divider"></div>

    <ul class="contact">
      <li class="contact__item">
        <svg class="contact__icon" viewBox="0 0 24 24" aria-hidden="true"><path d="M6.6 10.8a15.1 15.1 0 0 0 6.6 6.6l2.2-2.2a1 1 0 0 1 1-.25 11.4 11.4 0 0 0 3.6.57 1 1 0 0 1 1 1V20a1 1 0 0 1-1 1A17 17 0 0 1 3 4a1 1 0 0 1 1-1h3.5a1 1 0 0 1 1 1c0 1.25.2 2.45.57 3.57a1 1 0 0 1-.25 1z"/></svg>
        <span>(+357) 25-704263</span>
      </li>
      <li class="contact__item">
        <svg class="contact__icon" viewBox="0 0 24 24" aria-hidden="true"><path d="M2 5h20v14H2z M4 7v.5l8 5.5 8-5.5V7z" fill-rule="evenodd"/></svg>
        <span>info@dorvelanfit.example</span>
      </li>
      <li class="contact__item">
        <svg class="contact__icon" viewBox="0 0 24 24" aria-hidden="true"><path d="M12 2a7 7 0 0 0-7 7c0 5.2 7 13 7 13s7-7.8 7-13a7 7 0 0 0-7-7zm0 9.5A2.5 2.5 0 1 1 12 6.5a2.5 2.5 0 0 1 0 5z"/></svg>
        <span>Limassol, Cyprus 12-14<br>Stavrinelou str,<br>Ano Trimeni,P.C. 4832</span>
      </li>
    </ul>
  </section>

</body>
</html>
```